電子書籍の表紙デザインをお願い致します。

本の内容、
冴えない20代のOLでした。そんな私でしたが約7年前に、
「たった一度きりのこの人生。もっと自分らしく、もっと輝かせたい。」
と強く熱望した瞬間があり、私は知識・人脈・実績・経験・貯金などビジネスに関してプラスになるような持ち合わせが一切ないゼロの状態で、【私らしい生き方と働き方】を一心に求めて「起業」を目指しはじめました。
今では独立を果たし、当時は未知の世界でしかなかった独立起業の道も今年で7年目に突入しました。得意な分野は、ビジネスコンサルティング、ビジネスプロデュース、コミュニティ運営、Webマーケティング、Webライティング、アフィリエイト、プロモーション、マインドコーチング、オウンドメディア構築など。写真や動画の編集・加工などクリエイティブなことも割と好きです。

私の仕事における共通点はどのビジネスでもパソコン1台とネット環境があれば場所を問わずどこでも仕事ができることです。そのライフスタイルを「スカイハーベスター」と名付け、よく国内外問わず、大好きな旅をしながら仕事をしています。

しかし、この 「起業」という働き方に出会う前の私は、好きなことをしながら仕事ができる、そんなワークスタイルがあるだなんて夢にも思っていませんでした。
そんなの理想のまた理想・・・そんなかんじで。しかしそれ以上に私が伝えたいのは、「自分でビジネスをして価値提供をする」という中で自分の思考や価値観、ライフスタイルまでも大きく変化したということなのです。そして今は毎日に充実感があり、やりがいを感じながら仕事も楽しくしています。

そして現在は、自らの経験と海外で得た感動をもとにPC1台で好きな時に・好きな場所で・好きな人と、「自分らしく、グローバルに生きていく」そんなスタイルを日々全力で、熱狂してご提供しています。

優しい雰囲気の安心できるような女性らしいカラーでお願い致します。

使って頂きたい画像と本文を添付致します。
表紙はこの4枚の画像を使って優しいイメージで、パステルカラー、薄い色を使っていただけると嬉しいです。

タイトルは
きみの毎日は花になる!扉をそっと叩いて
心ほどける日々を選び取るための小さな習慣集
でお願い致します。

はじめに、私の起業ストーリーを少しお話しさせてください。私はもともと自分に自信がまったく持てなくて、そのくせ社会不適合で、ただただ路頭に迷う、冴えない20代のOLでした。そんな私でしたが約7年前に、

日にちを19日まで延長させていただきました。
20日まで延長致しました。宜しくお願い致します。
いま、
最終段階で決定に向けて進めております。
21日で締め切らせていただきます。最後までよろしくお願いいたします。

お洒落な大人女子のイメージややんわりとしたパステルカラーの色合いがとても美しい作品だと感じました。タイトルや入れたい文字をしっかりと目立たせていただきました。自分の思い描くイメージをカタチにしてくださったなと感謝の想いでいっぱいでございます。

この度、ご提案してくださったデザイナーの皆様、最後まで吟味させて頂き、選ぶのにとても迷いました。それほど、素晴らしい作品ばかりでした。沢山のご提案を本当に有難うございました。今回はご縁を頂けなかった皆様とも、今後も定期的にコンペをさせていただく予定ですので、どうぞよろしくお願いします。

```html
<!DOCTYPE html>
<html lang="ja">
<head>
<meta charset="UTF-8">
<title>心ほどける日々を選び取るための小さな習慣集</title>
<link rel="stylesheet" href="https://fonts.googleapis.com/css2?family=M+PLUS+Rounded+1c:wght@500;800&family=Zen+Old+Mincho:wght@700&family=Kaushan+Script&display=swap">
<style>
  :root {
    --bg-pink: #f6c9dc;
    --bg-lilac: #d9d2f2;
    --bg-sky: #bfe3f5;
    --bg-cream: #f7f1c8;
    --panel: #fffdfb;
    --line: #d9c6b3;
    --ink: #3a3337;
    --pink: #e8609a;
    --brown: #8a5a3b;
    --gold: #d2a66a;
    --gold-dark: #a97b43;
    --brand: #8aa3bf;
  }
  * { box-sizing: border-box; margin: 0; padding: 0; }
  html, body { width: 750px; height: 1200px; overflow: hidden; }
  body { background: #fff; }
  .cover {
    position: relative; width: 750px; height: 1200px; overflow: hidden;
    background:
      radial-gradient(circle at 90% 8%, var(--bg-cream) 0, transparent 38%),
      linear-gradient(120deg, var(--bg-pink) 0%, var(--bg-lilac) 45%, var(--bg-sky) 100%);
  }
  .photo {
    position: absolute; border: 10px solid #fff;
    box-shadow: 0 6px 14px rgba(80,60,90,.25);
  }
  .photo--group { left: 36px; top: 14px; width: 230px; height: 172px; transform: rotate(-3deg);
    background: linear-gradient(160deg, #d7e6d0, #b48d74 55%, #6d5a52); }
  .photo--terrace { left: 16px; top: 862px; width: 230px; height: 300px; transform: rotate(-5deg);
    background: linear-gradient(170deg, #9fd0f0 0%, #f2e6d2 45%, #c9b79d 75%, #7ab8c9 100%); }
  .photo--garden { left: 262px; top: 872px; width: 218px; height: 296px; transform: rotate(4deg);
    background: linear-gradient(170deg, #b7d6a6 0%, #e49bb4 40%, #6f9a5e 75%, #c9b8a4 100%); }
  .photo--forest { left: 478px; top: 852px; width: 250px; height: 180px; transform: rotate(5deg);
    background: linear-gradient(160deg, #6f9a59 0%, #a8c68a 45%, #e9e0cf 70%, #5d7c48 100%); }
  .brand {
    position: absolute; left: 380px; top: 88px;
    display: flex; align-items: center; gap: 12px;
    font-family: "M PLUS Rounded 1c", sans-serif; font-weight: 500;
    font-size: 36px; color: var(--brand); letter-spacing: 1px;
  }
  .brand__dot { width: 14px; height: 14px; border-radius: 50%; background: var(--brand); }
  .panel {
    position: absolute; left: 50px; top: 212px; width: 655px; height: 632px;
    background: var(--panel); box-shadow: 0 4px 18px rgba(120,100,140,.18);
  }
  .panel::before {
    content: ""; position: absolute; inset: 12px; border: 1.5px solid var(--line);
  }
  .sparkle { position: absolute; left: 315px; top: 26px; width: 26px; height: 26px; }
  .lead {
    position: absolute; left: 92px; top: 66px; width: 470px; height: 74px;
  }
  .lead svg { position: absolute; inset: 0; width: 100%; height: 100%; }
  .lead__text {
    position: relative; display: block; text-align: center; line-height: 74px;
    font-family: "Zen Old Mincho", serif; font-size: 40px; color: var(--brown);
    font-style: italic;
  }
  .title { position: absolute; left: 0; top: 160px; width: 655px; text-align: center;
    font-family: "M PLUS Rounded 1c", sans-serif; font-weight: 800; color: var(--ink); }
  .title__line { display: block; white-space: nowrap; }
  .title__line--1 { font-size: 60px; line-height: 90px; }
  .title__line--2 { font-size: 72px; line-height: 100px; color: var(--pink); }
  .title__line--3 { font-size: 72px; line-height: 100px; }
  .accent { color: var(--pink); }
  .ribbon { position: absolute; left: 40px; top: 500px; width: 575px; height: 96px; }
  .ribbon svg { position: absolute; inset: 0; width: 100%; height: 100%; }
  .ribbon__text {
    position: relative; display: block; text-align: center; line-height: 82px;
    font-family: "M PLUS Rounded 1c", sans-serif; font-weight: 800; font-size: 56px;
    color: #fff; letter-spacing: 4px;
  }
  .author { position: absolute; right: 36px; top: 1108px; line-height: 1;
    font-family: "Kaushan Script", cursive; font-size: 62px; color: var(--brown); }
  .author__mark { font-family: "M PLUS Rounded 1c", sans-serif; font-weight: 500; font-size: 26px; margin-left: 6px; }
</style>
</head>
<body>
<main class="cover">
  <div class="photo photo--group" role="img" aria-label="仲間たちと並ぶ集合写真"></div>

  <div class="brand">
    <span class="brand__dot" aria-hidden="true"></span>
    <span class="brand__name">Sky Harvester</span>
  </div>

  <section class="panel">
    <svg class="sparkle" viewBox="0 0 24 24" aria-hidden="true">
      <path d="M12 0 L14 10 L24 12 L14 14 L12 24 L10 14 L0 12 L10 10 Z" fill="var(--gold)"/>
    </svg>
    <div class="lead">
      <svg viewBox="0 0 470 74" preserveAspectRatio="none" aria-hidden="true">
        <path d="M10 4 H460 L446 37 L460 70 H10 L24 37 Z" fill="#f6ece0" stroke="var(--line)" stroke-width="1.5"/>
      </svg>
      <span class="lead__text">きみの毎日は花になる!</span>
    </div>
    <h1 class="title">
      <span class="title__line title__line--1">扉をそっと叩いて</span>
      <span class="title__line title__line--2">心ほどける日々を</span>
      <span class="title__line title__line--3"><span class="accent">選び取る</span>ための</span>
    </h1>
    <div class="ribbon">
      <svg viewBox="0 0 575 96" preserveAspectRatio="none" aria-hidden="true">
        <path d="M0 20 H44 V90 H0 L18 55 Z" fill="var(--gold-dark)"/>
        <path d="M575 20 H531 V90 H575 L557 55 Z" fill="var(--gold-dark)"/>
        <rect x="30" y="4" width="515" height="78" rx="4" fill="var(--gold)"/>
        <rect x="38" y="11" width="499" height="64" rx="3" fill="none" stroke="#fff" stroke-width="1.5" stroke-dasharray="4 4"/>
      </svg>
      <span class="ribbon__text">小さな習慣集</span>
    </div>
  </section>

  <div class="photo photo--terrace" role="img" aria-label="南国のテラスとプールの写真"></div>
  <div class="photo photo--garden" role="img" aria-label="バラのアーチが咲く庭園の写真"></div>
  <div class="photo photo--forest" role="img" aria-label="緑の森で岩に腰掛ける旅の写真"></div>

  <div class="author">Hinata<span class="author__mark">著</span></div>
</main>
</body>
</html>
```